Wellspring Renewal Collective Botswana Africa Flyer

Create an A5 double sided flyer to advertise a campus lifestyle wellness training at the university of Tselakgang. This flyer invite all interested to freely attend naturopathic treatment training, stop addiction training, music therapy training lessons. Conducted by Wellspring Renewal Collective. The lead facilitator is Marisol-Ann Okoye.
Flyer text available at 'must haves'

Target Market(s)

University students

Industry/Entity Type

Training

Requirements
Must have
• Logo (supplied)
• Picture of Marisol-Ann Okoye, our Lead Facilitator (supplied)
• Music pic. Classical hym choir or preferably orchestra of predominantly black youth
• And the text must be as follows:
• WELLSPRING RENEWAL COLLECTIVE (WRC) is a non profit organization that conducts wholistic health programs in Universities aimed at reversing Lifestyle Diseases and breaking down the chains of Drug Addiction and Satanism among the youth. We conduct a 3 hour practical training every week on disease treatment protocols, stop addiction and music therapy.
• 1. Disease Treatment Programs: We thoroughly train you to use food, herbs, natural remedies and scientifically proven lifestyle changes to reverse lifestyle diseases such as diabetes, arthritis, cancer and hypertension.
• 2. Stop Addiction Programs: We also teach you how to administer a 10 day treatment protocol to wipe out the craving for drugs such cocaine, marijuana and tobacco, and to also rehabilitate those freed from these addictions.
• 3. Music Therapy: Top notch musical training will equip you to efficiently administer music therapy to heal the soul and relief tensions in any community using voice and musical instruments. Music, when properly done, heals both the singer and the one to whom it is sung!
• These training protocols will not only help you but most importantly will equip you to effectively help others!
• THE MUSIC CONNECTION
• Music is part of our being. There is a kind of music that goes to the waist igniting in us the desire for illicit sex, drugs and all recklessness. And there is a type of music that touches the heart and bring us closer to our Maker, igniting feelings of sympathy, kindness and generosity to our fellow man.
• When we are happy, a song always says it best. When we are sad, music has a way of saying it in ways that words would never reach. And when there is a call to action, a cause to which the sleeping needs to be awakened, music makes a perfect wake up call!
• The cause of WRC is a liberation struggle that cannot do without music. For when the chains of addiction are broken down, the joy that comes cannot be expressed in talking tones. And since it was through music that our captivity was perpetuated, it's only befitting that our liberation must be sustained through song. It is a new song though, which we shall first learn to sing in voice, and then through musical instruments of harps, violins and keyboards. A Quadrangle Ensemble of Daybreak, singing Meadowlight Hymns! You ought to be a part of it!
• THIS VALUABLE TRAINING THAT IS WORTH LOTS OF MONEY ELSEWHERE IS NOW BROUGHT TO YOU FREE OF CHARGE. TO ENROLL IMMEDIATELY CALL 71450362 or EMAIL: WRC2016@kelvora.com

```html
<!DOCTYPE html>
<html lang="en">
<head>
<meta charset="utf-8">
<title>Wellspring Renewal Collective – Campus Wellness Training Flyer</title>
<link rel="stylesheet" href="https://fonts.googleapis.com/css2?family=Pontano+Sans&family=Roboto+Condensed:wght@400;700&family=Playball&display=swap">
<style>
  :root{
    --ground:#e9e7e2;
    --paper:#ffffff;
    --green:#8cc63f;
    --green-deep:#5fa32b;
    --green-wash:#eef5e2;
    --green-wash-2:#d9e9c4;
    --red:#d7282f;
    --orange:#f39a1e;
    --yellow:#f7ee2a;
    --ink:#222222;
    --ink-soft:#3b3b3b;
    --white:#ffffff;
    --body:"Pontano Sans", Arial, sans-serif;
    --cond:"Roboto Condensed", "Arial Narrow", sans-serif;
    --script:"Playball", cursive;
  }
  *{box-sizing:border-box;margin:0;padding:0}
  html,body{width:1200px;height:871px;overflow:hidden}
  body{background:var(--ground);position:relative;font-family:var(--body);color:var(--ink)}

  .page{position:absolute;top:36px;width:566px;height:800px;background:var(--paper);overflow:hidden;box-shadow:0 2px 8px rgba(0,0,0,.18)}
  .page--front{left:24px}
  .page--back{left:610px;background:linear-gradient(180deg,#f6faef 0%,var(--green-wash) 45%,var(--green-wash-2) 100%)}

  /* FRONT */
  .header{position:absolute;left:0;top:0;width:100%;height:150px}
  .wordmark{position:absolute;left:26px;top:38px;width:150px;display:flex;align-items:center;gap:8px}
  .wordmark__dot{width:18px;height:18px;border-radius:50%;background:var(--red);flex:none}
  .wordmark__name{font-family:var(--cond);font-weight:700;font-size:14px;line-height:1.15;color:var(--green-deep)}
  .header__rule{position:absolute;left:190px;top:34px;width:1px;height:80px;background:#bbbbbb}
  .intro{position:absolute;left:204px;top:34px;width:335px;font-size:10.6px;line-height:1.42;color:var(--ink-soft)}
  .intro strong{font-family:var(--cond);color:var(--ink)}
  .swoosh{position:absolute;left:0;top:112px;width:566px;height:60px}

  .photo{position:absolute;left:0;top:158px;width:566px;height:318px;background:linear-gradient(160deg,#6b4a36 0%,#3a5a8f 40%,#c9a77f 70%,#4d2f5e 100%)}

  .band{position:absolute;left:0;top:476px;width:566px;height:64px;background:var(--green);color:var(--white);font-family:var(--cond);font-weight:700;text-transform:uppercase;text-align:center;padding-top:10px}
  .band__lead{font-size:19.5px;line-height:1.1}
  .band__sub{font-size:15px;line-height:1.3}

  .programs{position:absolute;left:0;top:540px;width:566px;height:260px;background:linear-gradient(180deg,#ffffff 0%,var(--green-wash) 100%)}
  .program{position:absolute;left:0;width:362px;padding-left:74px}
  .program__num{position:absolute;left:24px;top:8px;width:40px;height:40px;border-radius:50%;background:var(--red);color:var(--white);font-family:var(--cond);font-weight:700;font-size:24px;display:flex;align-items:center;justify-content:center}
  .program__title{font-family:var(--cond);font-size:14px;color:var(--ink);margin-bottom:2px}
  .program__text{font-size:9.4px;line-height:1.4;color:var(--ink-soft)}
  .program--1{top:18px}
  .program--2{top:88px}
  .program--3{top:158px}

  .note{position:absolute;left:378px;top:28px;width:164px;height:180px;background:var(--yellow);transform:rotate(-3deg);box-shadow:2px 4px 6px rgba(0,0,0,.2);padding:34px 12px 0 18px;font-family:var(--cond);font-size:15px;line-height:1.4;color:var(--ink)}
  .note__pin{position:absolute;left:82px;top:-6px;width:26px;height:26px}

  /* BACK */
  .frame{position:absolute;left:14px;top:14px;width:538px;height:772px;border:1px solid #b9d39a}
  .music-art{position:absolute;left:336px;top:20px;width:220px;height:420px;border-radius:110px 0 0 110px;background:radial-gradient(ellipse at 60% 40%,rgba(60,60,60,.35) 0%,rgba(120,120,120,.15) 45%,rgba(255,255,255,0) 75%)}
  .tree-art{position:absolute;left:230px;top:470px;width:170px;height:300px;background:radial-gradient(ellipse at 50% 40%,rgba(90,110,80,.22) 0%,rgba(90,110,80,0) 70%)}
  .title{position:absolute;left:86px;top:34px;font-family:var(--script);font-weight:400;font-size:40px;line-height:1.05;color:var(--ink)}
  .title span{display:block;padding-left:60px}
  .copy{position:absolute;font-size:10.6px;line-height:1.46;color:var(--ink-soft)}
  .copy--a{left:84px;top:142px;width:290px}
  .copy--b{left:84px;top:240px;width:300px}
  .copy--c{left:66px;top:322px;width:450px}
  .copy--c strong{font-family:var(--cond);font-weight:700;color:var(--ink)}

  .offer{position:absolute;left:14px;top:472px;width:538px;height:86px;background:var(--green);font-family:var(--cond);font-weight:700;font-size:14.5px;line-height:1.35;text-align:center;text-transform:uppercase;color:var(--ink);padding-top:16px}

  .portrait{position:absolute;left:46px;top:568px;width:114px;height:114px;border-radius:50%;border:5px solid var(--white);background:radial-gradient(circle at 50% 40%,#c89c7e 0%,#6f4a34 60%,#3d2a1f 100%);box-shadow:0 1px 4px rgba(0,0,0,.25)}
  .facilitator{position:absolute;left:20px;top:690px;width:166px;text-align:center}
  .facilitator__name{font-family:var(--cond);font-weight:700;font-size:14px;color:var(--ink)}
  .facilitator__role{font-size:11px;font-style:italic;color:var(--ink-soft)}

  .wordmark--back{left:392px;top:710px;width:150px}
  .wordmark--back .wordmark__name{font-size:12px}
</style>
</head>
<body>

<section class="page page--front" aria-label="Flyer front">
  <header class="header">
    <div class="wordmark">
      <span class="wordmark__dot"></span>
      <span class="wordmark__name">WELLSPRING RENEWAL COLLECTIVE</span>
    </div>
    <div class="header__rule"></div>
    <p class="intro"><strong>WELLSPRING RENEWAL COLLECTIVE (WRC)</strong> is a non profit organization that conducts wholistic health programs in Universities aimed at reversing Lifestyle Diseases and breaking down the chains of Drug Addiction and Satanism among the youth.</p>
  </header>

  <svg class="swoosh" viewBox="0 0 566 60" preserveAspectRatio="none" aria-hidden="true">
    <path d="M0 40 C150 10 350 0 566 26 L566 60 L0 60 Z" fill="var(--green)"/>
    <path d="M0 34 C160 6 360 -2 566 20 L566 28 C360 6 160 14 0 46 Z" fill="var(--orange)"/>
    <path d="M0 28 C170 2 370 -6 566 12 L566 20 C370 0 170 10 0 38 Z" fill="var(--red)"/>
  </svg>

  <div class="photo" role="img" aria-label="Photograph of a smiling youth choir singing together"></div>

  <div class="band">
    <div class="band__lead">We conduct a 3 hour practical training every week on</div>
    <div class="band__sub">Disease treatment protocols, stop addiction and music therapy</div>
  </div>

  <div class="programs">
    <div class="program program--1">
      <span class="program__num">1</span>
      <h3 class="program__title">Disease Treatment Programs</h3>
      <p class="program__text">We thoroughly train you to use food, herbs, natural remedies and scientifically proven lifestyle changes to reverse lifestyle diseases such as diabetes, arthritis, cancer and hypertension.</p>
    </div>
    <div class="program program--2">
      <span class="program__num">2</span>
      <h3 class="program__title">Stop Addiction Programs</h3>
      <p class="program__text">We also teach you how to administer a 10 day treatment protocol to wipe out the craving for drugs such cocaine, marijuana and tobacco, and to also rehabilitate those freed from these addictions.</p>
    </div>
    <div class="program program--3">
      <span class="program__num">3</span>
      <h3 class="program__title">Music Therapy</h3>
      <p class="program__text">Top notch musical training will equip you to efficiently administer music therapy to heal the soul and relief tensions in any community using voice and musical instruments. Music, when properly done, heals both the singer and the one to whom it is sung!</p>
    </div>

    <div class="note">
      <svg class="note__pin" viewBox="0 0 26 26" aria-hidden="true">
        <line x1="8" y1="20" x2="13" y2="12" stroke="#777" stroke-width="2"/>
        <circle cx="15" cy="9" r="7" fill="var(--red)"/>
      </svg>
      These training protocols will not only help you but most importantly will equip you to effectively help others!
    </div>
  </div>
</section>

<section class="page page--back" aria-label="Flyer back">
  <div class="frame"></div>
  <div class="music-art" role="img" aria-label="Decorative treble clef with swirling music staff and notes"></div>
  <div class="tree-art" role="img" aria-label="Faint silhouette of a tree"></div>

  <h2 class="title">The Music <span>Connection</span></h2>

  <p class="copy copy--a">Music is part of our being. There is a kind of music that goes to the waist igniting in us the desire for illicit sex, drugs and all recklessness. And there is a type of music that touches the heart and bring us closer to our Maker, igniting feelings of sympathy, kindness and generosity to our fellow man.</p>
  <p class="copy copy--b">When we are happy, a song always says it best. When we are sad, music has a way of saying it in ways that words would never reach. And when there is a call to action, a cause to which the sleeping needs to be awakened, music makes a perfect wake up call!</p>
  <p class="copy copy--c"><strong>The cause of WRC is a liberation struggle that cannot do without music.</strong><br>For when the chains of addiction are broken down, the joy that comes cannot be expressed in talking tones. And since it was through music that our captivity was perpetuated, it's only befitting that our liberation must be sustained through song. It is a new song though, which we shall first learn to sing in voice, and then through musical instruments of harps, violins and keyboards. A Quadrangle Ensemble of Daybreak, singing Meadowlight Hymns! You ought to be a part of it!</p>

  <div class="offer">
    This valuable training that is worth lots of money<br>
    elsewhere is now brought to you free of charge.<br>
    To enroll immediately call 71450362 | Email. WRC2016@kelvora.com
  </div>

  <div class="portrait" role="img" aria-label="Portrait photo of Marisol-Ann Okoye, Lead Facilitator"></div>
  <div class="facilitator">
    <div class="facilitator__name">Marisol-Ann Okoye</div>
    <div class="facilitator__role">Lead Facilitator</div>
  </div>

  <div class="wordmark wordmark--back">
    <span class="wordmark__dot"></span>
    <span class="wordmark__name">WELLSPRING RENEWAL COLLECTIVE</span>
  </div>
</section>

</body>
</html>
```